Tailbrook Website Design

Need a website for a Dog Grooiming business. Please make it simular to these:

https://www.furvanto.com
https://haulnorix.com
https://meadowpetrin.com
https://www.drivelumo.com/search/

```html
<!DOCTYPE html>
<html lang="en">
<head>
<meta charset="utf-8">
<title>Tailbrook – Doorstep Dog Grooming</title>
<link href="https://fonts.googleapis.com/css2?family=Roboto:wght@400;500;700;900&display=swap" rel="stylesheet">
<style>
:root{
  --navy:#0d3570;
  --navy-dark:#0a2c5e;
  --teal:#22c7a0;
  --teal-btn:#2ccaa6;
  --blue:#1a8ff0;
  --link-blue:#1478e6;
  --ink:#1b1b1b;
  --muted:#555;
  --footer:#141414;
  --white:#fff;
}
*{box-sizing:border-box;margin:0;padding:0}
html,body{width:1200px;height:4093px;overflow:hidden}
body{position:relative;font-family:"Roboto",Arial,sans-serif;color:var(--ink);background:var(--white)}

/* header */
.site-header{position:absolute;left:0;top:0;width:1200px;height:80px;background:var(--white)}
.brand{position:absolute;left:98px;top:14px;font-size:44px;font-weight:700;color:var(--navy);letter-spacing:-.5px}
.head-info{position:absolute;top:10px;display:flex;align-items:center;gap:8px}
.head-info .ico{width:40px;height:40px;border-radius:50%;background:var(--navy);display:flex;align-items:center;justify-content:center}
.head-info small{display:block;font-size:12px;color:#333;text-transform:uppercase}
.head-info strong{font-size:18px;font-weight:500;color:#222}
.head-info .phone{color:var(--link-blue);font-weight:700}
.flag{display:inline-block;width:30px;height:17px;background:linear-gradient(#b22 0 50%,#fff 50% 100%);vertical-align:-2px;margin-right:4px;position:relative}
.flag:before{content:"";position:absolute;left:0;top:0;width:13px;height:9px;background:#2a3d7a}

.main-nav{position:absolute;left:0;top:80px;width:1200px;height:57px;background:var(--navy)}
.main-nav a{position:absolute;top:20px;font-size:15px;font-weight:500;color:var(--white);text-decoration:none}
.main-nav a.active{color:var(--teal)}

/* hero */
.hero{position:absolute;left:0;top:137px;width:1200px;height:594px;background:linear-gradient(100deg,#eef1f4 0%,#e3e7ea 45%,#c9d3da 75%,#9fc8dd 100%)}
.hero h1{position:absolute;left:96px;top:150px;font-size:52px;line-height:50px;font-weight:700;color:#111}
.hero p{position:absolute;left:99px;top:268px;font-size:22px;line-height:26px;font-weight:500;color:#111}
.btn-pill{display:inline-flex;align-items:center;justify-content:center;gap:8px;border-radius:30px;font-weight:500;color:var(--white);text-decoration:none}
.hero .btn-pill{position:absolute;left:100px;top:344px;width:162px;height:42px;background:var(--teal-btn);font-size:15px}
.dots{position:absolute;left:560px;top:562px;display:flex;gap:14px}
.dots i{width:10px;height:10px;border-radius:50%;background:rgba(255,255,255,.6)}
.dots i.on{background:var(--white)}

/* quote form */
.quote{position:absolute;left:736px;top:64px;width:337px;height:466px;background:var(--navy)}
.quote-head{height:88px;background:var(--teal);color:var(--white);font-size:27px;font-weight:700;line-height:33px;text-align:center;padding-top:12px}
.quote .field{position:absolute;left:12px;width:312px;height:41px;background:var(--white);font-size:13px;color:#333;padding:12px 14px}
.quote .caret{position:absolute;right:14px;top:17px;border:5px solid transparent;border-top:6px solid #111}
.quote .send{position:absolute;left:14px;top:406px;width:172px;height:45px;background:var(--teal-btn);font-size:13px}

/* signature */
.signature{position:absolute;left:0;top:731px;width:1200px;height:866px;background:linear-gradient(172deg,#22c9a0 0%,#1cbbb6 35%,#1aa3df 70%,#1a90f0 100%);color:var(--white)}
.van{position:absolute;left:72px;top:64px;width:548px;height:341px;border-radius:40px 120px 30px 30px;background:linear-gradient(160deg,#ffffff,#dde4ea)}
.signature h2{position:absolute;left:686px;top:104px;font-size:50px;line-height:52px;font-weight:700}
.signature .lead{position:absolute;left:686px;top:225px;font-size:22px;line-height:27px;font-weight:500}
.signature .contact{position:absolute;left:686px;top:292px;font-size:20px}
.signature .contact u{text-decoration:underline}
.ghost{position:absolute;top:345px;height:38px;border:2px solid var(--white);border-radius:22px;font-size:16px;display:flex;align-items:center;justify-content:center;gap:8px;font-weight:500}
.arc{position:absolute;left:0;top:0}
.svc-icon{position:absolute;width:88px;height:88px;border-radius:50%;background:var(--white);border:6px solid rgba(255,255,255,.35);background-clip:padding-box;display:flex;align-items:center;justify-content:center}
.svc-label{position:absolute;font-size:22px;line-height:30px;font-weight:500}
.svc-label.r{text-align:right}
.tub{position:absolute;left:429px;top:564px;width:310px;height:294px;border-radius:120px 120px 20px 20px;background:linear-gradient(180deg,#c8a67e,#a87a4c)}

/* video */
.video{position:absolute;left:0;top:1597px;width:1200px;height:540px;background:linear-gradient(90deg,#d9cbbf 0%,#b77a48 45%,#8b5a33 55%,#d6d3cf 80%,#ececec 100%)}
.play{position:absolute;left:568px;top:228px;width:84px;height:84px;border-radius:50%;background:var(--white);display:flex;align-items:center;justify-content:center}

/* testimonials */
.section-title{position:absolute;left:0;width:1200px;text-align:center;font-size:36px;font-weight:500;color:#111}
.review{position:absolute;top:2288px;width:320px;height:243px;background:var(--white);box-shadow:0 0 8px rgba(0,0,0,.12);padding:20px}
.review .avatar{position:absolute;left:20px;top:20px;width:58px;height:58px;border-radius:50%;background:#d9d2cc}
.review .name{position:absolute;left:90px;top:28px;font-size:15px;font-weight:700}
.review .meta{position:absolute;left:90px;top:50px;font-size:12px;color:#777}
.review .meta b{color:#f3a81c;font-weight:400;letter-spacing:1px}
.review p{position:absolute;left:20px;top:90px;width:290px;font-size:14px;line-height:30px;color:#333}
.review .more{position:absolute;left:20px;top:212px;font-size:14px;font-weight:700;color:var(--teal)}

/* cta */
.cta{position:absolute;left:0;top:2614px;width:1200px;height:376px;background:linear-gradient(90deg,#1a8ff0 0%,#1ba7d8 50%,#22c9a0 100%);color:var(--white);text-align:center}
.cta h2{position:absolute;left:0;top:94px;width:1200px;font-size:38px;font-weight:700}
.cta p{position:absolute;left:300px;top:158px;width:600px;font-size:14px;line-height:29px}
.cta .btn-pill{position:absolute;left:524px;top:235px;width:150px;height:43px;border:2px solid var(--white);font-size:15px}

/* gallery */
.tile{position:absolute;width:234px;height:234px}

/* footer */
.site-footer{position:absolute;left:0;top:3721px;width:1200px;height:372px;background:var(--footer);color:var(--white)}
.site-footer h4{position:absolute;top:82px;font-size:21px;font-weight:700}
.site-footer .link{position:absolute;font-size:15px}
.f-contact{position:absolute;left:464px;display:flex;align-items:center;gap:12px;font-size:15px;line-height:22px}
.f-contact .c{width:36px;height:36px;border-radius:50%;background:#2b2b2b;display:flex;align-items:center;justify-content:center;flex:none}
.subscribe{position:absolute;left:771px;top:179px;width:270px;height:42px;background:var(--white);color:#333;font-size:13px;padding:13px 15px}
.subscribe-btn{position:absolute;left:1051px;top:179px;width:48px;height:42px;background:#1d9bd8;display:flex;align-items:center;justify-content:center}
.social{position:absolute;top:240px;width:36px;height:36px;border-radius:50%;background:#2b2b2b}
.footer-rule{position:absolute;left:98px;top:310px;width:1002px;height:1px;background:#333}
.copyright{position:absolute;left:0;top:334px;width:1200px;text-align:center;font-size:15px}
</style>
</head>
<body>

<header class="site-header">
  <div class="brand">Tailbrook</div>
  <div class="head-info" style="left:725px">
    <span class="ico"><svg width="22" height="22" viewBox="0 0 24 24" fill="none" stroke="#fff" stroke-width="1.6"><circle cx="12" cy="12" r="9"/><path d="M3 12h18M12 3c3 3 3 15 0 18M12 3c-3 3-3 15 0 18"/></svg></span>
    <div><small>Your Location</small><strong><span class="flag"></span>USA</strong></div>
  </div>
  <div class="head-info" style="left:918px">
    <span class="ico"><svg width="20" height="20" viewBox="0 0 24 24" fill="#fff"><path d="M6.6 10.8a15 15 0 0 0 6.6 6.6l2.2-2.2c.3-.3.7-.4 1-.2 1.1.4 2.3.6 3.6.6.6 0 1 .4 1 1V20c0 .6-.4 1-1 1A17 17 0 0 1 3 4c0-.6.4-1 1-1h3.5c.6 0 1 .4 1 1 0 1.3.2 2.5.6 3.6.1.3 0 .7-.2 1z"/></svg></span>
    <div><small>Call us today</small><strong class="phone">800 - 555 - 0199</strong></div>
  </div>
</header>

<nav class="main-nav">
  <a class="active" style="left:98px">Home</a>
  <a style="left:191px">Locations</a>
  <a style="left:311px">Careers</a>
  <a style="left:413px">About</a>
  <a style="left:501px">Blog</a>
  <a style="left:578px">FAQ</a>
</nav>

<section class="hero" role="img" aria-label="Small terrier wrapped in a white bath towel with soap bubbles in a bright grooming room">
  <h1>Doorstep<br>Dog Grooming</h1>
  <p>Sed ut perspiciatis unde omnis iste<br>natus error sit voluptatem</p>
  <a class="btn-pill">Book Online <svg width="14" height="12" viewBox="0 0 14 12" fill="none" stroke="#fff" stroke-width="1.6"><path d="M1 6h11M8 2l4 4-4 4"/></svg></a>
  <div class="dots"><i></i><i></i><i class="on"></i><i></i></div>
</section>

<form class="quote">
  <div class="quote-head">Get Free Quotes from<br>Dog Specialists!</div>
  <div class="field" style="top:108px">Name*</div>
  <div class="field" style="top:158px">Email*</div>
  <div class="field" style="top:211px">Phone*</div>
  <div class="field" style="top:262px">Services<span class="caret"></span></div>
  <div class="field" style="top:313px;height:84px">Message</div>
  <a class="btn-pill send">GET QUOTE NOW</a>
</form>

<section class="signature">
  <div class="van" role="img" aria-label="White grooming van with paw print livery"></div>
  <h2>The Tailbrook<br>Signature Service</h2>
  <p class="lead">Sed ut perspiciatis unde omnis iste<br>natus error sit voluptatem</p>
  <p class="contact">(800) 555-0142 or <u>Book Online</u></p>
  <div class="ghost" style="left:686px;width:118px"><svg width="20" height="16" viewBox="0 0 20 16" fill="#fff"><path d="M1 1h12v8H6l-3 3V9H1zM15 5h4v8h-2v3l-3-3H8v-2h7z"/></svg>Text</div>
  <div class="ghost" style="left:817px;width:118px"><svg width="16" height="16" viewBox="0 0 24 24" fill="#fff"><path d="M6.6 10.8a15 15 0 0 0 6.6 6.6l2.2-2.2c.3-.3.7-.4 1-.2 1.1.4 2.3.6 3.6.6.6 0 1 .4 1 1V20c0 .6-.4 1-1 1A17 17 0 0 1 3 4c0-.6.4-1 1-1h3.5c.6 0 1 .4 1 1 0 1.3.2 2.5.6 3.6.1.3 0 .7-.2 1z"/></svg>Call</div>

  <svg class="arc" width="1200" height="866" viewBox="0 0 1200 866" fill="none" stroke="rgba(255,255,255,.8)" stroke-width="3">
    <path d="M283 866 C283 640 420 505 600 505 C780 505 915 640 915 866"/>
  </svg>
  <div class="tub" role="img" aria-label="Two French bulldog puppies in a wooden bath tub with shampoo bottles and towels"></div>

  <div class="svc-icon" style="left:410px;top:501px"><svg width="38" height="38" viewBox="0 0 24 24" fill="none" stroke="#1a8ff0" stroke-width="1.4"><path d="M3 12h18v2a5 5 0 0 1-5 5H8a5 5 0 0 1-5-5zM7 19l-1 2M17 19l1 2M8 9a4 4 0 0 1 8 0"/></svg></div>
  <div class="svc-label r" style="left:170px;top:516px;width:212px">Warm Filtered<br>Water Bath</div>

  <div class="svc-icon" style="left:701px;top:501px"><svg width="38" height="38" viewBox="0 0 24 24" fill="none" stroke="#1a8ff0" stroke-width="1.4"><circle cx="15" cy="10" r="5"/><path d="M10 10H3M12 14l-2 7h3l1-6M4 7l-2-1M4 13l-2 1"/></svg></div>
  <div class="svc-label" style="left:806px;top:516px">Gentle Brush &amp;<br>Blowout</div>

  <div class="svc-icon" style="left:286px;top:617px"><svg width="38" height="38" viewBox="0 0 24 24" fill="none" stroke="#1a8ff0" stroke-width="1.4"><rect x="4" y="10" width="8" height="11" rx="1"/><path d="M6 10V7h4v3M14 6h5v15h-5zM16 3h1v3"/></svg></div>
  <div class="svc-label r" style="left:60px;top:631px;width:210px">All Natural<br>Products</div>

  <div class="svc-icon" style="left:824px;top:617px"><svg width="38" height="38" viewBox="0 0 24 24" fill="none" stroke="#1a8ff0" stroke-width="1.4"><circle cx="8" cy="18" r="3"/><circle cx="16" cy="18" r="3"/><path d="M9 15l5-12M15 15L10 3"/></svg></div>
  <div class="svc-label" style="left:928px;top:631px">Trim &amp;<br>File Nails</div>

  <div class="svc-icon" style="left:239px;top:747px"><svg width="38" height="38" viewBox="0 0 24 24" fill="none" stroke="#1a8ff0" stroke-width="1.4"><rect x="4" y="3" width="9" height="9" rx="1"/><path d="M8 12v9M15 8l5 10M20 8l-5 10"/></svg></div>
  <div class="svc-label r" style="left:20px;top:764px;width:202px">Breed Specific<br>Pro Groom</div>

  <div class="svc-icon" style="left:871px;top:747px"><svg width="38" height="38" viewBox="0 0 24 24" fill="none" stroke="#1a8ff0" stroke-width="1.4"><path d="M10 4l1.5 5L16 10l-4.5 1.5L10 16l-1.5-4.5L4 10l4.5-1zM18 3l.7 2 2 .7-2 .7L18 8l-.7-1.6-2-.7 2-.7zM18 15l.7 2 2 .7-2 .7-.7 1.6-.7-1.6-2-.7 2-.7z"/></svg></div>
  <div class="svc-label" style="left:976px;top:764px">Clean Teeth &amp;<br>Ears</div>
</section>

<section class="video" role="img" aria-label="Groomers brushing a fluffy chow chow and drying a small dog in a grooming salon">
  <div class="play"><svg width="22" height="24" viewBox="0 0 22 24"><path d="M2 1l19 11L2 23z" fill="#1a8ff0"/></svg></div>
</section>

<h2 class="section-title" style="top:2222px">Testimonials</h2>
<article class="review" style="left:98px">
  <div class="avatar" role="img" aria-label="Customer portrait"></div>
  <div class="name">John Smith</div>
  <div class="meta"><b>★★★★★</b> (2days ago)</div>
  <p>Lorem ipsum dolor sit amet, consectetur adipiscing elit, sed do ed ter incididunt ut labore et dolore magqua. Quis ipsum suspendisse ultrices gravida.</p>
  <div class="more">Read More...</div>
</article>
<article class="review" style="left:439px">
  <div class="avatar" role="img" aria-label="Customer portrait"></div>
  <div class="name">John Smith</div>
  <div class="meta"><b>★★★★★</b> (2days ago)</div>
  <p>Lorem ipsum dolor sit amet, consectetur adipiscing elit, sed do ed ter incididunt ut labore et dolore magqua. Quis ipsum suspendisse ultrices gravida.</p>
  <div class="more">Read More...</div>
</article>
<article class="review" style="left:780px">
  <div class="avatar" role="img" aria-label="Customer portrait"></div>
  <div class="name">John Smith</div>
  <div class="meta"><b>★★★★★</b> (2days ago)</div>
  <p>Lorem ipsum dolor sit amet, consectetur adipiscing elit, sed do ed ter incididunt ut labore et dolore magqua. Quis ipsum suspendisse ultrices gravida.</p>
  <div class="more">Read More...</div>
</article>

<section class="cta" role="img" aria-label="Groomer at work, tinted blue to teal">
  <h2>Get Your Dog Grooiming Today.</h2>
  <p>Lorem ipsum dolor sit amet, consectetur adipiscing elit, seiusmod tempor incididunt ut labore et dolore magna aliqua. Quis ipsum pendisse</p>
  <a class="btn-pill">Contact Us</a>
</section>

<h2 class="section-title" style="top:3076px">Follow On @Tailbrook</h2>
<div class="tile" style="left:108px;top:3143px;background:linear-gradient(135deg,#efe6df,#c9ae98)" role="img" aria-label="Poodle puppy being trimmed"></div>
<div class="tile" style="left:358px;top:3143px;background:linear-gradient(135deg,#e7e2dc,#c98a45)" role="img" aria-label="Pomeranian being brushed"></div>
<div class="tile" style="left:607px;top:3143px;background:linear-gradient(135deg,#b9c6cf,#f4f2ef)" role="img" aria-label="White Maltese with a red bow"></div>
<div class="tile" style="left:855px;top:3143px;background:linear-gradient(135deg,#d8d4cf,#c9954f)" role="img" aria-label="Golden retriever under a shower"></div>
<div class="tile" style="left:108px;top:3388px;background:linear-gradient(135deg,#e6e4df,#b9c64f)" role="img" aria-label="Terrier wrapped in a green towel"></div>
<div class="tile" style="left:358px;top:3388px;background:linear-gradient(135deg,#7b7775,#b58a55)" role="img" aria-label="Yorkshire terrier being groomed"></div>
<div class="tile" style="left:607px;top:3388px;background:linear-gradient(135deg,#d7cdc1,#8a7a68)" role="img" aria-label="Pug resting on a blanket"></div>
<div class="tile" style="left:855px;top:3388px;background:linear-gradient(135deg,#eee9e4,#d0913f)" role="img" aria-label="Pomeranian with a grooming brush"></div>

<footer class="site-footer">
  <h4 style="left:100px">Quick Links</h4>
  <span class="link" style="left:100px;top:132px">Locations</span>
  <span class="link" style="left:100px;top:164px">Careers</span>
  <span class="link" style="left:100px;top:196px">About</span>
  <span class="link" style="left:100px;top:229px">Blog</span>
  <span class="link" style="left:100px;top:261px">FAQ</span>

  <h4 style="left:281px">Other Links</h4>
  <span class="link" style="left:281px;top:132px">Privacy Policy</span>
  <span class="link" style="left:281px;top:164px">Terms of Service</span>
  <span class="link" style="left:281px;top:196px">Credit</span>
  <span class="link" style="left:281px;top:229px">FAQ</span>

  <h4 style="left:464px">Contact Us</h4>
  <div class="f-contact" style="top:128px"><span class="c"><svg width="14" height="18" viewBox="0 0 14 18" fill="#fff"><path d="M7 0a7 7 0 0 1 7 7c0 5-7 11-7 11S0 12 0 7a7 7 0 0 1 7-7zm0 4a3 3 0 1 0 0 6 3 3 0 0 0 0-6z"/></svg></span><span>48 Larkfield Lane Springdale<br>USA&nbsp; 20145</span></div>
  <div class="f-contact" style="top:192px"><span class="c"><svg width="15" height="15" viewBox="0 0 24 24" fill="#fff"><path d="M6.6 10.8a15 15 0 0 0 6.6 6.6l2.2-2.2c.3-.3.7-.4 1-.2 1.1.4 2.3.6 3.6.6.6 0 1 .4 1 1V20c0 .6-.4 1-1 1A17 17 0 0 1 3 4c0-.6.4-1 1-1h3.5c.6 0 1 .4 1 1 0 1.3.2 2.5.6 3.6.1.3 0 .7-.2 1z"/></svg></span><span>202-555-0173</span></div>
  <div class="f-contact" style="top:244px"><span class="c"><svg width="16" height="12" viewBox="0 0 16 12" fill="none" stroke="#fff" stroke-width="1.4"><rect x="1" y="1" width="14" height="10"/><path d="M1 1l7 6 7-6"/></svg></span><span>info@tailbrook.com</span></div>

  <h4 style="left:771px">Keep Updated</h4>
  <span class="link" style="left:771px;top:126px;width:330px;line-height:23px">Lorem ipsum dolor sit amet, cocr adipiscing elit, sed do eiusmod tempor incididunt ut</span>
  <div class="subscribe">Your Email</div>
  <div class="subscribe-btn"><svg width="18" height="16" viewBox="0 0 18 16" fill="#fff"><path d="M0 7L18 0l-4 16-5-5-3 3V10l8-7-9 6z"/></svg></div>
  <span class="social" style="left:771px"></span>
  <span class="social" style="left:818px"></span>
  <span class="social" style="left:865px"></span>
  <span class="social" style="left:912px"></span>

  <div class="footer-rule"></div>
  <div class="copyright">Copyright © 2021 Tailbrook. All rights reserved.</div>
</footer>

</body>
</html>
```